Content Management company needs a new brochure

We help companies transform their content (rework it so it easier to write, read, find, use and share). We work in the topic base structured authoring industry; think information design and the technology needed to create, share and publish exception content. We need a brochure that sells our services while giving us a moderns and progressive identify.

WARNING: our website, www.lumarotext.com is being updated. We are moving away from the tree metaphor. Don't use it.

UPDATED....... MAY 13, 2015, 2PM EDT..............

SIZE: All must be US Letter size (8.5 x 11)
Logo files are attached.

This project consists of 3 deliverables:

1. Credit Union Brochure:
I have attached new copy. Ideally this is 1 page; front and back.

2. Before & After example:
Matching the credit union brochure layout, we would like the before and after example. B&A mock-up and source documents attached.

3. What is Lumaro Text
This is one pager that explains our offering. I would love to see this document in the style of this https://us.pixbarrow.com/id/52817306

Other styles I like:
http://blog.quorvastudio.com/wp-content/uploads/2012/10/Pine-brochure2.jpg
https://www.zelbrix.com/pt/paperwell
http://www.deckvault.net/brindlecorp/metadata-extraction-and-content-transformation

Target Market(s)

We sell to executive level management at medium to large companies in various sectors. This brochure is focussed on Credit Unions, but we'll need designs for insurance, healthcare, high-tech, etc.

Industry/Entity Type

It Company

Font styles to use
Sans Serif

Colors
0455a3
0792cd
3176b5
85acd3
d2a4cc
b768aa
f68d4c
0292cd
f37122

Requirements
Must have
• Needs to look slick. Not too busy.
Nice to have
• Can't think of anything. We are open to all designs.
Should not have

```html
<!DOCTYPE html>
<html lang="en">
<head>
<meta charset="utf-8">
<title>Lumaro Text — Benefit and Core Service</title>
<link rel="stylesheet" href="https://fonts.googleapis.com/css2?family=Raleway:ital,wght@0,400;0,500;1,600&display=swap">
<style>
  :root {
    --teal: #2fa9c9;
    --teal-text: #3aaccb;
    --teal-soft: #bfe4ee;
    --teal-pale: #e3f3f7;
    --paper: #ffffff;
  }
  * { box-sizing: border-box; margin: 0; padding: 0; }
  html, body { width: 928px; height: 1200px; overflow: hidden; background: var(--paper); }
  .page {
    position: relative;
    width: 928px;
    height: 1200px;
    overflow: hidden;
    background: var(--paper);
    font-family: "Raleway", sans-serif;
    color: var(--teal-text);
  }
  .texture { position: absolute; inset: 0; width: 928px; height: 1200px; }
  .section { position: absolute; }
  .section-title {
    font-style: italic;
    font-weight: 600;
    font-size: 27px;
    color: var(--teal);
    padding-bottom: 6px;
    border-bottom: 1.5px solid var(--teal);
    margin-bottom: 20px;
    letter-spacing: 0.2px;
  }
  .section p, .section li {
    font-size: 13px;
    line-height: 17.6px;
    font-weight: 400;
  }
  .section p + p, .section p + ul { margin-top: 17.6px; }
  .benefit { left: 115px; top: 286px; width: 226px; }
  .benefit p, .benefit li { text-align: justify; }
  .benefit ul { list-style: none; margin-top: 17.6px; }
  .benefit li::before { content: "•"; margin-right: 6px; }
  .core-service { left: 395px; top: 398px; width: 456px; }
  .core-service p { text-align: justify; }
  .core-service ul { list-style: none; }
  .core-service li { padding-left: 17px; position: relative; }
  .core-service li::before { content: "•"; position: absolute; left: 2px; }
</style>
</head>
<body>
<main class="page">
  <svg class="texture" viewBox="0 0 928 1200" role="img" aria-label="Halftone dot pattern in teal filling a large circular shape at the top right and a broad circular field at the lower left">
    <defs>
      <radialGradient id="lowerField" cx="0.45" cy="0.45" r="0.6">
        <stop offset="0" stop-color="var(--teal-pale)"/>
        <stop offset="0.55" stop-color="var(--teal-pale)"/>
        <stop offset="1" stop-color="var(--teal-soft)"/>
      </radialGradient>
      <linearGradient id="upperField" x1="0" y1="0" x2="0.3" y2="1">
        <stop offset="0" stop-color="var(--teal-soft)"/>
        <stop offset="1" stop-color="#d3edf4"/>
      </linearGradient>
    </defs>
    <circle cx="760" cy="-110" r="440" fill="url(#upperField)"/>
    <circle cx="1000" cy="330" r="180" fill="var(--paper)"/>
    <circle cx="300" cy="860" r="420" fill="url(#lowerField)"/>
    <rect x="0" y="1050" width="700" height="150" fill="var(--teal-soft)" opacity="0.6"/>
  </svg>

  <section class="section benefit">
    <h2 class="section-title">Benefit:</h2>
    <p>Start managing your content like an asset using Lumaro Text ™ and your company will benefit from</p>
    <ul>
      <li>improved content quality and control at a granular level</li>
      <li>improved findability of content</li>
      <li>cost reductions in creating, sharing and maintaining content</li>
      <li>increased consistency, compliance, and accuracy, and</li>
      <li>extensive multi-channel publishing capabilities (HTML, PDFs, Online Help, Wikis, Nortlake DeskShare, Nortlake Writer, RTF, ePub, and many others that you and your customer may need).</li>
    </ul>
  </section>

  <section class="section core-service">
    <h2 class="section-title">Our Core Service</h2>
    <p>We excel at helping credit unions upgrade and transform their high-value content.</p>
    <p>We partner with you to define, design and building solutions that fit your budget and existing systems. We then equip your organization with the tools and training needed to sustain and grow your new content and content practices.</p>
    <p>Our team of communication experts and information architects are highly-skilled and experienced in</p>
    <ul>
      <li>information governance</li>
      <li>content strategy</li>
      <li>topic-based structured authoring</li>
      <li>taxonomy and metadata design</li>
      <li>semantic markup</li>
      <li>content audits and inventory</li>
      <li>new media publishing</li>
      <li>project management</li>
      <li>process improvement, and</li>
      <li>usability testing.</li>
    </ul>
  </section>
</main>
</body>
</html>
```